Label for Refill packaging eco-conscious beauty brand

We need a label for our refill pouch. Velvet Harbor is an unscented conditioner formulated using the finest healthy & pure ingredients, free of chemicals and harmful toxins. As a minimalist beauty brand we are proud to be certified with TQB, Norvamark and Silver Kestrel.

We already have the pouches and an exciting label for our regular bottles.
We choose a kraft brown packing for the refill pouch and would like something minimalist but elegant for the label.

```html
<!DOCTYPE html>
<html lang="en">
<head>
<meta charset="utf-8">
<title>Velvet Harbor – Refill Pouch Label</title>
<link rel="stylesheet" href="https://fonts.googleapis.com/css2?family=Montserrat:wght@300;400&display=swap">
<style>
  :root {
    --backdrop: #ecebe9;
    --kraft: #b89573;
    --kraft-dark: #a9835f;
    --kraft-light: #c3a283;
    --gold: #d9ad2c;
    --gold-light: #f0cd52;
    --gold-dark: #b98d17;
    --ink-brown: #5a4128;
    --print-white: #f7f4ef;
  }
  * { margin: 0; padding: 0; box-sizing: border-box; }
  html, body {
    width: 1200px;
    height: 800px;
    overflow: hidden;
    background: var(--backdrop);
  }
  .canvas {
    position: relative;
    width: 1200px;
    height: 800px;
  }
  .pouch-label {
    position: absolute;
    left: 370px;
    top: 20px;
    width: 460px;
    height: 760px;
    border-radius: 14px;
    background: linear-gradient(90deg, var(--kraft-dark) 0%, var(--kraft) 12%, var(--kraft-light) 50%, var(--kraft) 88%, var(--kraft-dark) 100%);
    overflow: hidden;
    font-family: "Montserrat", sans-serif;
    color: var(--print-white);
  }
  .zip-track {
    position: absolute;
    left: 0;
    width: 100%;
    height: 1px;
    background: rgba(90, 65, 40, 0.25);
  }
  .zip-track.upper { top: 82px; }
  .zip-track.lower { top: 108px; }
  .brand-band {
    position: absolute;
    top: 0;
    left: 170px;
    width: 120px;
    height: 210px;
    background: linear-gradient(135deg, var(--gold-dark) 0%, var(--gold) 35%, var(--gold-light) 55%, var(--gold) 75%, var(--gold-dark) 100%);
    display: flex;
    flex-direction: column;
    align-items: center;
    justify-content: flex-end;
    padding-bottom: 26px;
  }
  .brand-mark {
    width: 14px;
    height: 14px;
    background: var(--print-white);
    margin-bottom: 44px;
  }
  .brand-name {
    font-weight: 400;
    font-size: 25px;
    line-height: 1.2;
    text-align: center;
    color: var(--print-white);
  }
  .leaf-art {
    position: absolute;
    left: 0;
    top: 0;
    width: 460px;
    height: 760px;
  }
  .product-title {
    position: absolute;
    top: 362px;
    width: 100%;
    text-align: center;
    font-weight: 300;
    font-size: 68px;
    line-height: 78px;
    letter-spacing: 0.5px;
  }
  .product-type {
    position: absolute;
    top: 538px;
    width: 100%;
    text-align: center;
    font-weight: 300;
    font-size: 14px;
    line-height: 17px;
  }
  .refill-tag {
    position: absolute;
    top: 610px;
    width: 100%;
    text-align: center;
    font-weight: 300;
    font-size: 14px;
  }
  .net-volume {
    position: absolute;
    top: 664px;
    width: 100%;
    text-align: center;
    font-weight: 300;
    font-size: 14px;
  }
</style>
</head>
<body>
<main class="canvas">
  <section class="pouch-label">
    <div class="zip-track upper"></div>
    <div class="zip-track lower"></div>

    <svg class="leaf-art" viewBox="0 0 460 760" role="img" aria-label="Fine line illustration of a skeleton leaf, drawn diagonally across the pouch">
      <defs>
        <radialGradient id="leafTone" cx="50%" cy="50%" r="50%">
          <stop offset="0%" stop-color="#8c6a48" stop-opacity="0.45"/>
          <stop offset="100%" stop-color="#8c6a48" stop-opacity="0.2"/>
        </radialGradient>
      </defs>
      <ellipse cx="230" cy="470" rx="120" ry="270" transform="rotate(-28 230 470)" fill="url(#leafTone)"/>
    </svg>

    <div class="brand-band">
      <span class="brand-mark"></span>
      <p class="brand-name">KLAAR<br>Mira</p>
    </div>

    <h1 class="product-title">Velvet<br>Harbor</h1>
    <p class="product-type">unscented hair conditioner<br>après-shampoing non parfumé</p>
    <p class="refill-tag">refill</p>
    <p class="net-volume">238ml ℮ / 8fl oz</p>
  </section>
</main>
</body>
</html>
```